Motivational Poster Design Project

I would like to create a poster with some of my favorite quotes to hang in my office. I did a similar project in 2012 and I've uploaded the top 2 designs so you can get a better idea of what I'm looking for. I will provide feedback on your design within 24 hours of receiving it.

The poster must contain the following quotes:

"You’re only given a little spark of madness. You mustn’t lose it.”
- Dorian Halbrook

“The most contrarian thing of all is not to oppose the crowd but to think for yourself.”
- Marcus Vell

"I constantly see people rise in life who are not the smartest, sometimes not even the most diligent, but they are learning machines. They go to bed every night a little wiser than they were when they got up and boy does that help, particularly when you have a long run ahead of you."
- Walter Brisco

“In theory, there’s no difference between theory and practice. But, in practice, there is.”
- Piet R. K. Ter Wolvenkamp

"At the end of the day, a reactionary life is a normal life. One thing is consistent in every remarkable person: they decide to do something remarkable. Don’t let the world choose who you become."
- Ravindra Kolpe

“It usually takes 3-4 months to try enough that you can do a proper 80/20 analysis, then two months to design systems to scale what *is* working.”
-Gus Ambery

“Authority is 20 percent given, 80 percent taken.”
- Harold Quimsby

“Your actions are consistent with the way the world occurs to you.”
- Anselm Grottke

Project Deadline Extended
Reason: I am going to be travelling with no access to internet until January 5th, 2015. I am extending the project deadline until 12/31/14 and I'll make a final decision during the 1st week of January.

Target Market(s)

Personal Project

Industry/Entity Type

Learning

Requirements
Must have
• The poster will be 24" high x 36" long and printed on canvas, so the image you create needs to have a resolution of at least 2700 x 3900.
Nice to have
• I don't have an exact vision for how the poster should look, so I am totally open to you using your creativity to develop, arrange and present the content as you'd like.
• That said, I would like an image (photo or posterized image) of the person being quoted along with each quote. I do not have specific images that I would like you to use, so you will need to find the images on your own. The images don't need to be perfect... I am more interested in the poster relating the essence of the quotes and the people being quoted than I am in perfect photographic images of the people being quoted.

```html
<!DOCTYPE html>
<html lang="en">
<head>
<meta charset="utf-8">
<title>Quotes Chalkboard Poster</title>
<link rel="stylesheet" href="https://fonts.googleapis.com/css2?family=Open+Sans:wdth,wght@75..100,400..700&family=Fondamento:ital@0;1&display=swap">
<style>
  :root {
    --wood-light: #b8946a;
    --wood-mid: #9a774f;
    --wood-dark: #6f5234;
    --board: #1b1b1b;
    --board-glow: #2c2c2c;
    --chalk: #f4f4f4;
    --pink: #f3a9c9;
    --blue: #93d4f2;
    --yellow: #f2ec8e;
    --lavender: #c7b9ee;
    --photo-light: #6e6e6e;
    --photo-dark: #242424;
  }
  * { box-sizing: border-box; margin: 0; padding: 0; }
  html, body { width: 1200px; height: 800px; overflow: hidden; background: var(--wood-mid); }
  .poster { position: relative; width: 1200px; height: 800px; overflow: hidden; }
  .frame {
    position: absolute; inset: 0;
    background: linear-gradient(90deg, var(--wood-dark) 0%, var(--wood-light) 12%, var(--wood-mid) 30%, var(--wood-light) 55%, var(--wood-mid) 78%, var(--wood-dark) 100%);
  }
  .board {
    position: absolute; left: 54px; top: 54px; width: 1092px; height: 690px;
    background: radial-gradient(ellipse at 50% 45%, var(--board-glow) 0%, var(--board) 70%, #141414 100%);
    box-shadow: 0 0 0 3px rgba(0,0,0,0.35), inset 0 0 40px rgba(0,0,0,0.6);
  }
  .portrait {
    position: absolute;
    background: radial-gradient(ellipse at 50% 40%, var(--photo-light) 0%, #4a4a4a 40%, var(--photo-dark) 80%, transparent 100%);
    border-radius: 45% 45% 20% 20%;
    opacity: 0.8;
  }
  .doodle { position: absolute; border-radius: 50%; opacity: 0.55; }
  .l {
    position: absolute; white-space: nowrap; line-height: 1;
    transform: translateY(-50%);
    color: var(--chalk);
    font-family: "Open Sans", sans-serif; font-weight: 400;
  }
  .l b { font-weight: 700; }
  .dense { font-stretch: 87%; }
  .name {
    position: absolute; white-space: nowrap; line-height: 1;
    transform: translateY(-50%);
    font-family: "Fondamento", cursive; font-style: italic; font-size: 24px;
  }
  .name.pink { color: var(--pink); }
  .name.blue { color: var(--blue); }
  .name.yellow { color: var(--yellow); }
  .name.lavender { color: var(--lavender); }
  .name.centered { transform: translate(-50%, -50%); text-align: center; }
  svg.chalk-art { position: absolute; overflow: visible; }
</style>
</head>
<body>
<div class="poster">
  <div class="frame" role="img" aria-label="Weathered wooden frame around the chalkboard"></div>
  <div class="board"></div>

  <svg class="chalk-art" style="left:66px;top:64px" width="70" height="62" viewBox="0 0 70 62">
    <polygon points="35,2 43,23 67,24 48,38 55,60 35,47 15,60 22,38 3,24 27,23" fill="#cfcfcf" opacity="0.85"/>
  </svg>
  <svg class="chalk-art" style="left:1060px;top:54px" width="86" height="86" viewBox="0 0 92 92">
    <polygon points="46,4 56,34 88,34 62,53 72,86 46,66 20,86 30,53 4,34 36,34" fill="none" stroke="var(--blue)" stroke-width="2.5"/>
  </svg>

  <!-- Dorian Halbrook -->
  <div class="portrait" style="left:120px;top:180px;width:102px;height:168px" role="img" aria-label="Black and white portrait of Dorian Halbrook"></div>
  <div class="doodle" style="left:72px;top:286px;width:56px;height:60px;background:radial-gradient(circle,var(--pink) 0%,transparent 70%)" role="img" aria-label="Chalk light bulb doodle"></div>
  <div class="l" style="left:134px;top:142px;font-size:19px">"You’re only given</div>
  <div class="l" style="left:144px;top:174px;font-size:19px">a <b style="font-size:24px">little spark</b> of</div>
  <div class="l" style="left:216px;top:214px;font-size:19px"><b style="font-size:27px">madness</b>.</div>
  <div class="l" style="left:234px;top:252px;font-size:19px">You mustn’t</div>
  <div class="l" style="left:238px;top:288px;font-size:19px"><b style="font-size:25px">lose</b> it.”</div>
  <div class="name pink" style="left:130px;top:364px">Dorian Halbrook</div>

  <!-- Marcus Vell -->
  <div class="portrait" style="left:372px;top:204px;width:126px;height:144px" role="img" aria-label="Black and white portrait of Marcus Vell speaking"></div>
  <div class="doodle" style="left:564px;top:258px;width:70px;height:70px;background:radial-gradient(circle,var(--blue) 0%,transparent 70%)" role="img" aria-label="Chalk sun and cloud doodle"></div>
  <div class="l" style="left:394px;top:126px;font-size:17px">“The <b style="font-size:21px">most contrarian</b></div>
  <div class="l" style="left:394px;top:157px;font-size:17px"><b style="font-size:21px">thing</b> of all is <b style="font-size:21px">not to</b></div>
  <div class="l" style="left:418px;top:190px;font-size:17px"><b style="font-size:21px">oppose</b> the crowd but</div>
  <div class="l" style="left:488px;top:220px;font-size:17px"><b style="font-size:21px">to think</b> for</div>
  <div class="l" style="left:504px;top:250px;font-size:17px"><b style="font-size:21px">yourself</b>.”</div>
  <div class="name blue" style="left:422px;top:354px">Marcus Vell</div>

  <!-- Walter Brisco -->
  <div class="portrait" style="left:708px;top:210px;width:102px;height:132px" role="img" aria-label="Black and white portrait of Walter Brisco speaking"></div>
  <svg class="chalk-art" style="left:806px;top:274px" width="92" height="60" viewBox="0 0 94 66">
    <polyline points="2,62 20,44 32,54 52,26 64,38 88,6" fill="none" stroke="var(--yellow)" stroke-width="2.5"/>
    <polyline points="74,6 88,6 88,20" fill="none" stroke="var(--yellow)" stroke-width="2.5"/>
  </svg>
  <div class="l dense" style="left:674px;top:103px;font-size:10.5px">"I constantly see people rise in life who are not</div>
  <div class="l dense" style="left:674px;top:122px;font-size:10.5px"><b style="font-size:14px">the smartest</b>, sometimes not even</div>
  <div class="l dense" style="left:674px;top:144px;font-size:10.5px"><b style="font-size:14px">the most diligent</b>, but they are</div>
  <div class="l dense" style="left:674px;top:168px;font-size:10.5px"><b style="font-size:14px">learning machines</b>. They <b style="font-size:14px">go to</b></div>
  <div class="l dense" style="left:674px;top:190px;font-size:10.5px"><b style="font-size:14px">bed every night</b> a little wiser than</div>
  <div class="l dense" style="left:674px;top:210px;font-size:10.5px">they were when they <b style="font-size:14px">got up</b> and boy does</div>
  <div class="l dense" style="left:679px;top:232px;font-size:10.5px">that help,</div>
  <div class="l dense" style="left:797px;top:232px;font-size:10.5px"><b style="font-size:14px">particularly</b></div>
  <div class="l dense" style="left:672px;top:253px;font-size:10.5px">when you</div>
  <div class="l dense" style="left:804px;top:253px;font-size:10.5px">have a <b style="font-size:14px">long</b></div>
  <div class="l dense" style="left:674px;top:275px;font-size:10.5px"><b style="font-size:14px">run</b></div>
  <div class="l dense" style="left:828px;top:275px;font-size:10.5px"><b style="font-size:14px">ahead</b></div>
  <div class="l dense" style="left:674px;top:295px;font-size:10.5px"><b style="font-size:14px">of</b></div>
  <div class="l dense" style="left:816px;top:295px;font-size:10.5px"><b style="font-size:14px">you</b>."</div>
  <div class="name yellow" style="left:672px;top:350px">Walter Brisco</div>

  <!-- Piet R. K. Ter Wolvenkamp -->
  <div class="portrait" style="left:996px;top:228px;width:96px;height:108px" role="img" aria-label="Black and white portrait of Piet R. K. Ter Wolvenkamp"></div>
  <div class="l" style="left:936px;top:124px;font-size:15px">“In theory, there’s <b style="font-size:20px">no</b></div>
  <div class="l" style="left:936px;top:154px;font-size:15px"><b style="font-size:20px">difference</b> between</div>
  <div class="l" style="left:936px;top:187px;font-size:15px"><b style="font-size:20px">theory</b> and <b style="font-size:20px">practice</b>.</div>
  <div class="l" style="left:936px;top:220px;font-size:15px">But, <b style="font-size:20px">in practice</b>,</div>
  <div class="l" style="left:932px;top:250px;font-size:15px"><b style="font-size:20px">there is</b>.”</div>
  <div class="name blue centered" style="left:1022px;top:352px">Piet R. K. Ter</div>
  <div class="name blue centered" style="left:1022px;top:380px">Wolvenkamp</div>

  <!-- Ravindra Kolpe -->
  <div class="portrait" style="left:120px;top:492px;width:96px;height:126px" role="img" aria-label="Black and white portrait of Ravindra Kolpe"></div>
  <div class="doodle" style="left:74px;top:596px;width:70px;height:68px;border:2px solid var(--yellow);background:transparent" role="img" aria-label="Chalk globe doodle"></div>
  <div class="l" style="left:90px;top:436px;font-size:12px">“At the end of the day, a <b style="font-size:16px">reactionary</b></div>
  <div class="l" style="left:90px;top:461px;font-size:12px"><b style="font-size:16px">life</b> is a <b style="font-size:16px">normal life</b>. One thing is</div>
  <div class="l" style="left:90px;top:490px;font-size:12px"><b style="font-size:16px">consistent</b> in every <b style="font-size:16px">remarkable</b></div>
  <div class="l" style="left:222px;top:517px;font-size:12px"><b style="font-size:16px">person</b> : they</div>
  <div class="l" style="left:222px;top:544px;font-size:12px"><b style="font-size:16px">decide to do</b></div>
  <div class="l" style="left:222px;top:571px;font-size:12px">something remarkable.</div>
  <div class="l" style="left:160px;top:600px;font-size:12px"><b style="font-size:16px">Don’t let the world</b></div>
  <div class="l" style="left:160px;top:631px;font-size:12px"><b style="font-size:16px">choose</b> who you become."</div>
  <div class="name yellow" style="left:138px;top:670px">Ravindra Kolpe</div>

  <!-- Gus Ambery -->
  <div class="portrait" style="left:414px;top:504px;width:84px;height:108px" role="img" aria-label="Black and white portrait of Gus Ambery smiling"></div>
  <svg class="chalk-art" style="left:366px;top:558px" width="132" height="144" viewBox="0 0 132 144">
    <polyline points="4,2 4,140 130,140" fill="none" stroke="var(--yellow)" stroke-width="2"/>
    <polyline points="8,124 32,86 54,100 80,56 100,70 126,34" fill="none" stroke="var(--yellow)" stroke-width="2"/>
    <polyline points="8,132 34,106 58,112 84,76 106,84 126,56" fill="none" stroke="var(--yellow)" stroke-width="2" stroke-dasharray="6 5"/>
  </svg>
  <div class="l" style="left:394px;top:431px;font-size:13px">“It usually takes <b style="font-size:17px">3-4 months</b></div>
  <div class="l" style="left:394px;top:461px;font-size:13px"><b style="font-size:17px">to try enough</b> that you can</div>
  <div class="l" style="left:394px;top:491px;font-size:13px">do a proper <b style="font-size:17px">80/20 analysis</b>,</div>
  <div class="l" style="left:494px;top:518px;font-size:13px">then two months</div>
  <div class="l" style="left:490px;top:546px;font-size:13px">to <b style="font-size:17px">design</b></div>
  <div class="l" style="left:494px;top:574px;font-size:13px">systems to <b style="font-size:17px">scale</b></div>
  <div class="l" style="left:494px;top:601px;font-size:13px"><b style="font-size:17px">what *is*</b></div>
  <div class="l" style="left:494px;top:629px;font-size:13px"><b style="font-size:17px">working</b>.”</div>
  <div class="name yellow" style="left:468px;top:672px">Gus Ambery</div>

  <!-- Harold Quimsby -->
  <div class="portrait" style="left:672px;top:516px;width:120px;height:132px" role="img" aria-label="Black and white portrait of Harold Quimsby gesturing"></div>
  <div class="doodle" style="left:806px;top:564px;width:30px;height:86px;border-radius:6px;background:linear-gradient(180deg,transparent,var(--pink) 60%,transparent)" role="img" aria-label="Chalk pencil doodle"></div>
  <div class="l" style="left:661px;top:439px;font-size:18px">“Authority is</div>
  <div class="l" style="left:661px;top:472px;font-size:18px"><b style="font-size:23px">20 percent given</b>,</div>
  <div class="l" style="left:661px;top:506px;font-size:18px"><b style="font-size:23px">80 percent</b></div>
  <div class="l" style="left:661px;top:542px;font-size:18px"><b style="font-size:23px">taken</b>.”</div>
  <div class="name pink" style="left:662px;top:662px">Harold Quimsby</div>

  <!-- Anselm Grottke -->
  <div class="portrait" style="left:984px;top:510px;width:102px;height:138px" role="img" aria-label="Black and white portrait of Anselm Grottke speaking"></div>
  <div class="doodle" style="left:1066px;top:526px;width:80px;height:80px;background:radial-gradient(circle,var(--lavender) 0%,transparent 70%)" role="img" aria-label="Chalk compass rose doodle"></div>
  <div class="l" style="left:912px;top:458px;font-size:17px">“Your <b style="font-size:20px">actions</b> are</div>
  <div class="l" style="left:912px;top:488px;font-size:17px"><b style="font-size:20px">consistent</b> with</div>
  <div class="l" style="left:912px;top:520px;font-size:17px">the way</div>
  <div class="l" style="left:912px;top:550px;font-size:17px">the world</div>
  <div class="l" style="left:912px;top:580px;font-size:17px"><b style="font-size:20px">occurs</b></div>
  <div class="l" style="left:912px;top:610px;font-size:17px"><b style="font-size:20px">to you</b>.”</div>
  <div class="name lavender" style="left:936px;top:674px">Anselm Grottke</div>
</div>
</body>
</html>
```